BENEATH THE [HARBOR] OF A DAWN, Mend your road

We are looking for a cover refresh of an existing bestselling book that is going into 3rd edition print this year.
The book is an inspirational as well as educational book that has become recognized as one of the most comprehensive, actionable, personal and financial planning resources available today for families, individuals and business owners alike.
Comprised of three true stories of loss, learning to live and love again and a 30 page checklist at the back of the book it contains tips and strategies for everyone to help them to get their personal and financial lives in order while they can.
The cover must have the following:
1. Appeal to a broad audience/both personal and corporate
2. Include Mara Quellton Bestselling Author
3. Include introduction of a new Afterword
4. 3rd Edition
5. Colors to remain the same – red, black and white
6. The title must remain in caps and the word [HARBOR] must have the brackets around it
We have also added a current copy of the second edition to help you. For your information our website is www.thequelltonhouse.example
Reason: We have narrowed it down to our top 3 designs. We are submitting the covers to our community for them to pick the top cover. Good luck to everyone

```html
<!DOCTYPE html>
<html lang="en">
<head>
<meta charset="utf-8">
<title>Beneath the [Harbor] of a Dawn — Mara Quellton</title>
<link href="https://fonts.googleapis.com/css2?family=Oswald:wght@300;500;600&family=Yellowtail&display=swap" rel="stylesheet">
<style>
  :root {
    --stage: #5b5b5b;
    --paper: #ffffff;
    --red: #e0322f;
    --badge: #ec6a4c;
    --ink: #333333;
    --art-light: #fbe3e2;
    --art-mid: #f2a9a6;
  }
  html, body {
    margin: 0;
    padding: 0;
    width: 667px;
    height: 1200px;
    overflow: hidden;
    background: var(--stage);
  }
  .cover {
    position: absolute;
    left: 43px;
    top: 151px;
    width: 580px;
    height: 897px;
    background: var(--paper);
    box-shadow: 0 10px 30px rgba(0,0,0,0.35);
    overflow: hidden;
  }
  .edition-badge {
    position: absolute;
    left: 451px;
    top: 13px;
    width: 100px;
    height: 100px;
    border-radius: 50%;
    background: var(--badge);
    color: var(--paper);
    display: flex;
    flex-direction: column;
    align-items: center;
    justify-content: center;
    font-family: "Oswald", sans-serif;
    font-weight: 600;
    font-size: 21px;
    line-height: 1.1;
  }
  .cover-art {
    position: absolute;
    left: 106px;
    top: 139px;
    width: 330px;
    height: 342px;
  }
  .title {
    position: absolute;
    left: 0;
    right: 0;
    top: 455px;
    display: flex;
    justify-content: center;
    align-items: flex-start;
    font-family: "Oswald", sans-serif;
    color: var(--red);
  }
  .title-lead {
    display: flex;
    flex-direction: column;
    align-items: flex-end;
    font-weight: 600;
    font-size: 24px;
    line-height: 1.05;
    margin-top: 64px;
    margin-right: 8px;
  }
  .title-main {
    display: flex;
    flex-direction: column;
    align-items: flex-end;
  }
  .title-keyword {
    font-weight: 500;
    font-size: 104px;
    line-height: 1.1;
    letter-spacing: 1px;
  }
  .title-keyword .bracket {
    color: var(--ink);
    font-weight: 300;
  }
  .title-tail {
    font-weight: 500;
    font-size: 24px;
    line-height: 1;
    margin-top: -8px;
    margin-right: 30px;
  }
  .subtitle {
    position: absolute;
    left: 0;
    right: 0;
    top: 640px;
    text-align: center;
    font-family: "Yellowtail", cursive;
    font-size: 64px;
    color: var(--red);
    line-height: 1;
  }
  .author-band {
    position: absolute;
    left: 0;
    right: 0;
    top: 805px;
    height: 52px;
    background: var(--red);
    display: flex;
    align-items: center;
    justify-content: center;
    font-family: "Oswald", sans-serif;
    font-weight: 500;
    font-size: 30px;
    letter-spacing: 12px;
    color: var(--paper);
    text-transform: uppercase;
  }
</style>
</head>
<body>
  <main class="cover">
    <div class="edition-badge"><span>3rd</span><span>Edition</span></div>

    <svg class="cover-art" role="img" aria-label="Illustration: red and white archery target with crosshair marks and a black fountain pen striking the bullseye" viewBox="0 0 330 342">
      <defs>
        <radialGradient id="art-fill" cx="0.5" cy="0.5" r="0.5">
          <stop offset="0" stop-color="var(--art-mid)"/>
          <stop offset="1" stop-color="var(--art-light)"/>
        </radialGradient>
      </defs>
      <rect width="330" height="342" fill="url(#art-fill)"/>
    </svg>

    <h1 class="title">
      <span class="title-lead"><span>BENEATH</span><span>THE</span></span>
      <span class="title-main">
        <span class="title-keyword"><span class="bracket">[</span>HARBOR<span class="bracket">]</span></span>
        <span class="title-tail">OF A DAWN</span>
      </span>
    </h1>

    <p class="subtitle">Mend your road</p>

    <div class="author-band">Mara Quellton</div>
  </main>
</body>
</html>
```